BOLD & MINIMALIST DESIGN NEEDED

We want a very bold but minimalistic business card design that is impactful and utilizes both sides of the business card. Our current logo is included for your use.

We want bold fonts and good use of negative space. We don't want the logo to overpower the design.

Target Market(s)

Professionals who are building new commercial buildings.

Industry/Entity Type

Construction

Contact Information for Business Card

Name, Title, email, office phone, cell phone, website

Font styles to use
Serif
Sans Serif

Requirements
Must have
• Bold design!

```html
<!DOCTYPE html>
<html lang="en">
<head>
<meta charset="utf-8">
<title>Ridgeline Design + Build — Business Card</title>
<link rel="stylesheet" href="https://fonts.googleapis.com/css2?family=Montserrat:wght@400;500;800&family=Oswald:wght@600&display=swap">
<style>
  :root {
    --page-bg: #161616;
    --card-white: #ffffff;
    --card-dark: #1d1d1d;
    --card-dark-edge: #2a2a2a;
    --ink: #1a1a1a;
    --ink-soft: #2b2b2b;
    --accent: #7cc12a;
    --decor-grey: #d4d4d4;
    --decor-green: #e6f4d6;
    --emboss: #0b0b0b;
  }
  * { margin: 0; padding: 0; box-sizing: border-box; }
  html, body {
    width: 1200px; height: 897px; overflow: hidden;
    background: var(--page-bg);
    font-family: "Montserrat", Arial, sans-serif;
  }
  .canvas { position: relative; width: 1200px; height: 897px; }

  .card {
    position: absolute; left: 304px; width: 594px; height: 338px;
    border-radius: 18px; overflow: hidden;
  }
  .card--front { top: 92px; background: var(--card-white); }
  .card--back {
    top: 470px;
    background: radial-gradient(ellipse at 60% 45%, var(--card-dark-edge), var(--card-dark) 70%);
  }

  .decor-panel {
    position: absolute; left: 0; top: 74px; width: 292px; bottom: 0;
    background: linear-gradient(90deg, var(--decor-grey) 0%, var(--decor-grey) 70%, var(--decor-green) 100%);
    opacity: 0.9;
  }

  .brand { position: absolute; text-align: center; }
  .brand__name {
    font-weight: 800; letter-spacing: 0.5px; line-height: 1;
    border-bottom: 2px solid currentColor; padding-bottom: 3px;
  }
  .brand__tag {
    font-weight: 500; letter-spacing: 6px; line-height: 1; margin-top: 4px;
  }
  .card--front .brand { left: 328px; top: 58px; color: var(--ink); width: 230px; }
  .card--front .brand__name { font-size: 37px; letter-spacing: 0; }
  .card--front .brand__tag { font-size: 13px; letter-spacing: 6.5px; }

  .person { position: absolute; left: 328px; top: 163px; }
  .person__name {
    font-family: "Oswald", "Arial Narrow", sans-serif; font-weight: 600;
    font-size: 31px; color: var(--accent); line-height: 1; letter-spacing: 0.3px;
  }
  .person__title { font-size: 13px; color: var(--ink-soft); margin-top: 4px; letter-spacing: 0.5px; }

  .contacts { position: absolute; left: 328px; top: 230px; list-style: none; }
  .contacts li {
    display: flex; align-items: center; gap: 6px;
    font-size: 14px; color: var(--ink); height: 18px;
  }
  .contacts svg { width: 12px; height: 12px; flex: none; }
  .contacts .highlight { color: var(--accent); }

  .card--back .brand { left: 0; right: 0; top: 138px; color: var(--emboss); }
  .card--back .brand__name {
    display: inline-block; font-size: 44px;
    text-shadow: 0 1px 0 rgba(255,255,255,0.09);
  }
  .card--back .brand__tag {
    font-size: 15px; letter-spacing: 10px; margin-top: 6px;
    text-shadow: 0 1px 0 rgba(255,255,255,0.09);
  }
</style>
</head>
<body>
<main class="canvas">
  <section class="card card--front" aria-label="Card front">
    <div class="decor-panel" role="img" aria-label="Large faint brand decoration in soft grey and pale green"></div>
    <div class="brand">
      <div class="brand__name">RIDGELINE</div>
      <div class="brand__tag">DESIGN + BUILD</div>
    </div>
    <div class="person">
      <div class="person__name">MARK DELANEY</div>
      <div class="person__title">OWNER</div>
    </div>
    <ul class="contacts">
      <li>
        <svg viewBox="0 0 12 12" aria-hidden="true"><path fill="#7cc12a" d="M2.3 0.8l1.6 0 .8 2.6-1.1.9a7 7 0 0 0 3.9 3.9l.9-1.1 2.6.8 0 1.6c0 .7-.6 1.2-1.3 1.2A9.7 9.7 0 0 1 1.1 2.1c0-.7.5-1.3 1.2-1.3z"/></svg>
        (555) 014-2380
      </li>
      <li>
        <svg viewBox="0 0 12 12" aria-hidden="true"><path fill="#7cc12a" d="M1 4.5C1 2.5 3 1.8 6 1.8s5 .7 5 2.7v.8H8.6v-.9H3.4v.9H1zM3 6.2h6l1.6 4.6H1.4z"/><circle cx="6" cy="8.3" r="1.1" fill="#fff"/></svg>
        (555) 014-2380
      </li>
      <li>
        <svg viewBox="0 0 12 12" aria-hidden="true"><rect x="0.8" y="2.3" width="10.4" height="7.4" fill="none" stroke="#7cc12a" stroke-width="1.2"/><path d="M0.8 2.5L6 6.6l5.2-4.1" fill="none" stroke="#7cc12a" stroke-width="1.2"/></svg>
        ridgelinebuild@mail.com
      </li>
      <li>
        <svg viewBox="0 0 12 12" aria-hidden="true"><g fill="none" stroke="#7cc12a" stroke-width="1"><circle cx="6" cy="6" r="5"/><ellipse cx="6" cy="6" rx="2.2" ry="5"/><path d="M1 6h10M2 3.3h8M2 8.7h8"/></g></svg>
        <span>www.<span class="highlight">ridgelinebuild</span>.com</span>
      </li>
    </ul>
  </section>

  <section class="card card--back" aria-label="Card back">
    <div class="brand">
      <div class="brand__name">RIDGELINE</div>
      <div class="brand__tag">DESIGN + BUILD</div>
    </div>
  </section>
</main>
</body>
</html>
```